thornbury good buys

i want a creative logo,and a webpage that looks like a e-commerce with a inner city,or a rural background, or anything that makes you notice the page,there is no limit to the creativity,it would have 8 categories,jewlry=3pgs,beauty=3pgs,kids baby-toy=2pgs,shirts=2pgs,shoes=2pgs,gaming=2pgs,watches=2pgs. all credit cards plus coinvaro acceptable,17 page total,the last page for secure billing.if there are any questions im here for you.

Target Market(s)

my target market is people that just might find something they like for a reasonable price

Industry/Entity Type

E-Commerce

Requirements
Must have
• payment options are a must,they set the table for everything
Nice to have
• items mentioned above plus creativity

```html
<!DOCTYPE html>
<html lang="en">
<head>
<meta charset="utf-8">
<title>Thornbury Good Buys</title>
<link href="https://fonts.googleapis.com/css2?family=Arimo:wght@400;700&family=Comfortaa:wght@400;700&family=Righteous&display=swap" rel="stylesheet">
<style>
:root{
  --header-top:#66759f;
  --header-bottom:#3c4a74;
  --navy:#3f4f7c;
  --tab-light:#f4f4f4;
  --tab-dark:#c9c9c9;
  --active-blue:#1a6ff0;
  --active-yellow:#f6d21a;
  --orange:#f25a0b;
  --green:#76a81b;
  --price:#e4480f;
  --panel-grey:#dcdcdc;
  --panel-blue:#c9d5f0;
  --text:#1e1e1e;
  --purple:#8a86c4;
  --sky:#2e8fe6;
  --sun:#ffd21f;
  --card-border:#d8d8d8;
}
*{box-sizing:border-box;margin:0;padding:0}
html,body{width:1200px;height:1149px;overflow:hidden;background:#fff;font-family:"Arimo",Arial,sans-serif;color:var(--text)}
.page{position:relative;width:1200px;height:1149px}

/* header */
.site-header{position:absolute;left:19px;top:0;width:1168px;height:183px;border-radius:0 0 14px 14px;background:linear-gradient(var(--header-top),var(--header-bottom))}
.brand{position:absolute;left:32px;top:30px;font-family:"Arimo",sans-serif;font-weight:700;color:#fff;line-height:1}
.brand-line1{font-size:50px;letter-spacing:3px}
.brand-line2{font-size:34px;letter-spacing:24px;margin-top:6px}
.top-links{position:absolute;right:42px;top:62px;color:#fff;font-size:16px;word-spacing:1px}
.main-nav{position:absolute;left:28px;top:134px;display:flex;height:48px}
.main-nav a{width:110px;height:48px;display:flex;align-items:center;justify-content:center;text-align:center;font-size:14px;font-weight:700;color:#222;text-decoration:none;line-height:1.05;background:linear-gradient(var(--tab-light),var(--tab-dark));border-right:2px solid #8f8f8f;border-radius:4px 4px 0 0}
.main-nav a.is-home{background:linear-gradient(#4aa0ff,var(--active-blue));color:#fff}
.main-nav a.is-returns{background:linear-gradient(#fff17a,var(--active-yellow))}

/* left sidebar */
.side-box{position:absolute;left:19px;width:244px;background:linear-gradient(#fff,#efefef);border:1px solid #dcdcdc;border-radius:4px;box-shadow:0 6px 6px -4px rgba(0,0,0,.35)}
.side-title{margin:6px 6px 0;height:28px;border-radius:4px;background:linear-gradient(#aaa,#7f7f7f);color:#fff;font-weight:700;font-size:15px;text-align:center;line-height:28px;letter-spacing:.5px}
.side-title.navy{background:var(--navy)}
.search-box{top:202px;height:105px}
.search-row{display:flex;align-items:center;gap:6px;margin:14px 0 0 14px}
.field{width:185px;height:26px;border:1px solid #ccc;background:#fff;font-size:13px;color:#999;padding:5px 8px}
.adv-link{display:block;text-align:center;font-size:12px;text-decoration:underline;color:#333;margin-top:4px;margin-right:20px}
.browse-box{top:333px;height:294px}
.cat-list{list-style:none;margin:10px 10px 0 10px}
.cat-list li{display:flex;align-items:center;gap:14px;height:26px;border-bottom:1px solid #dcdcdc;font-size:14px}
.cat-list li:last-child{border-bottom:0}
.bullet{width:16px;height:16px;border-radius:50%;background:linear-gradient(#a9c6d9,#5f8aa6);flex:none;display:flex;align-items:center;justify-content:center}
.news-box{top:650px;height:90px}
.news-row{display:flex;align-items:center;gap:8px;margin:14px 0 0 10px}
.news-row .field{width:182px}
.go-btn{width:30px;height:24px;border-radius:4px;background:#aaa;color:#fff;font-size:13px;text-align:center;line-height:24px;font-weight:700}
.bookmark-box{top:770px;height:90px}
.bookmark-title{display:flex;align-items:center;gap:6px;margin:10px 0 0 8px;font-size:13px;font-weight:700;color:#333}
.social-row{display:flex;gap:5px;margin:10px 0 0 6px}
.social-row span{width:36px;height:36px;border-radius:4px}
.pay-row{position:absolute;left:19px;top:902px;display:flex;gap:6px}
.pay-chip{width:44px;height:30px;border-radius:3px;border:1px solid #bbb;background:#f7f7f7;font-size:9px;font-weight:700;color:#3f4f7c;display:flex;align-items:center;justify-content:center}

/* center */
.summer-banner{position:absolute;left:276px;top:202px;width:609px;height:176px;border-radius:8px;background:radial-gradient(ellipse at 50% 90%,#ffe45a,var(--sun) 70%);overflow:hidden}
.summer-title{position:absolute;left:0;right:0;top:14px;text-align:center;font-family:"Righteous",sans-serif;font-size:38px;color:#fff;letter-spacing:2px}
.summer-title em{font-style:normal;color:var(--orange)}
.summer-strip{position:absolute;left:38px;top:60px;width:533px;height:22px;background:#fff;font-weight:700;font-size:15px;text-align:center;line-height:22px;letter-spacing:1px}
.summer-art{position:absolute;left:130px;top:92px;width:360px;height:84px;border-radius:6px 6px 0 0;background:linear-gradient(90deg,#575b63,#e58a5a,#4da65c,#e03a95)}
.section-head{position:absolute;left:286px;display:flex;align-items:center;gap:12px;font-size:28px;font-weight:700}
.section-head.featured{top:398px;color:var(--orange)}
.section-head.latest{top:686px;color:#111}
.product-panel{position:absolute;left:276px;width:609px;height:228px;border-radius:10px;display:flex;gap:19px;padding:11px 12px}
.product-panel.grey{top:439px;background:var(--panel-grey)}
.product-panel.blue{top:730px;background:var(--panel-blue);height:224px}
.product-card{width:101px;background:#fff;border:1px solid var(--card-border);border-radius:6px;display:flex;flex-direction:column;align-items:center;padding-top:6px}
.product-img{width:80px;height:100px;border-radius:4px}
.product-name{font-size:13px;text-align:center;line-height:1.05;margin-top:8px;height:30px}
.price{color:var(--price);font-weight:700;font-size:13px;margin-top:10px}
.buy-btn{margin-top:8px;width:84px;height:20px;border:1px solid #c9c9c9;border-radius:3px;background:linear-gradient(#fff,#e6e6e6);font-size:12px;font-weight:700;color:#1f63c9;display:flex;align-items:center;justify-content:center;gap:4px}

/* right column */
.promo{position:absolute;left:895px;width:289px;border-radius:6px;overflow:hidden}
.promo-offer{border:1px solid #d9d9d9;background:linear-gradient(#fff,#f1f1f1);box-shadow:0 4px 5px -3px rgba(0,0,0,.3)}
.offer-10{top:202px;height:150px}
.offer-25{top:375px;height:150px}
.promo-img{position:absolute;left:6px;top:20px;width:96px;height:110px;border-radius:4px}
.offer-text{position:absolute;left:112px;top:10px}
.offer-big{font-weight:700;font-size:34px;line-height:1.05}
.offer-10 .offer-big{color:var(--green)}
.offer-25 .offer-big{color:var(--orange)}
.offer-sub{font-size:18px;font-weight:700;margin-top:2px}
.offer-note{font-size:15px;color:#333;line-height:1.2;margin-top:6px}
.support{top:543px;height:138px;background:linear-gradient(#9a97d0,var(--purple));color:#fff}
.support-title{position:absolute;left:14px;top:8px;font-family:"Righteous",sans-serif;font-size:24px;line-height:1}
.support-title .hours{color:var(--sun)}
.support-note{position:absolute;left:14px;top:88px;font-size:13px;line-height:1.35}
.headset-icon{position:absolute;right:16px;top:16px}
.mega{top:703px;height:120px;background:linear-gradient(#6cc0ff 0 45%,var(--sky) 45%);color:#fff}
.mega-text{position:absolute;left:14px;top:10px;font-family:"Comfortaa",sans-serif;font-size:28px;line-height:1.05}
.mega-text strong{color:var(--sun);font-size:40px;font-weight:700;display:block}
.mega-arrow{position:absolute;right:12px;top:10px}

/* footer */
.site-footer{position:absolute;left:17px;top:986px;width:1155px;height:153px;background:linear-gradient(#f4f4f4,#e1e1e1);border-radius:4px}
.footer-col{position:absolute;top:12px;padding-right:26px;border-right:2px solid #c9c9c9;height:112px}
.footer-col:last-child{border-right:0}
.footer-col h3{font-weight:400;font-size:23px;color:#333;margin-bottom:10px}
.footer-col li{list-style:none;font-size:12px;color:#333;line-height:22px}
</style>
</head>
<body>
<div class="page">

<header class="site-header">
  <div class="brand">
    <div class="brand-line1">THORNBURY</div>
    <div class="brand-line2">GOOD BUYS</div>
  </div>
  <nav class="top-links">Value of the Day &nbsp;|&nbsp; Local Ad &nbsp;|&nbsp; Store Finder &nbsp;|&nbsp; Registry &nbsp;| Gift Cards</nav>
  <nav class="main-nav">
    <a class="is-home">Home</a><a>About</a><a>Gallery</a><a>Sale</a><a>T &amp; Cs</a><a>Postage &amp;<br>Delivery</a><a class="is-returns">Returns</a><a>Blog</a><a>Newly Added</a><a>Contact Us</a>
  </nav>
</header>

<aside>
  <section class="side-box search-box">
    <div class="side-title">Search the Product</div>
    <div class="search-row">
      <div class="field">Type the keyword</div>
      <svg width="22" height="22" viewBox="0 0 22 22"><circle cx="9" cy="9" r="6" fill="none" stroke="#555" stroke-width="2.5"/><line x1="13.5" y1="13.5" x2="20" y2="20" stroke="#555" stroke-width="3"/></svg>
    </div>
    <a class="adv-link">Advance Search</a>
  </section>

  <section class="side-box browse-box">
    <div class="side-title navy">Browse by Release</div>
    <ul class="cat-list">
      <li><span class="bullet"><svg width="8" height="8" viewBox="0 0 8 8"><path d="M2 1 L6 4 L2 7" fill="none" stroke="#fff" stroke-width="1.6"/></svg></span>Electronics &amp; Office</li>
      <li><span class="bullet"><svg width="8" height="8" viewBox="0 0 8 8"><path d="M2 1 L6 4 L2 7" fill="none" stroke="#fff" stroke-width="1.6"/></svg></span>Movies, Music &amp; Books</li>
      <li><span class="bullet"><svg width="8" height="8" viewBox="0 0 8 8"><path d="M2 1 L6 4 L2 7" fill="none" stroke="#fff" stroke-width="1.6"/></svg></span>Home</li>
      <li><span class="bullet"><svg width="8" height="8" viewBox="0 0 8 8"><path d="M2 1 L6 4 L2 7" fill="none" stroke="#fff" stroke-width="1.6"/></svg></span>Apparel, Shoes &amp; Jewelery</li>
      <li><span class="bullet"><svg width="8" height="8" viewBox="0 0 8 8"><path d="M2 1 L6 4 L2 7" fill="none" stroke="#fff" stroke-width="1.6"/></svg></span>Baby &amp; Kids</li>
      <li><span class="bullet"><svg width="8" height="8" viewBox="0 0 8 8"><path d="M2 1 L6 4 L2 7" fill="none" stroke="#fff" stroke-width="1.6"/></svg></span>Toys &amp; Video Games</li>
      <li><span class="bullet"><svg width="8" height="8" viewBox="0 0 8 8"><path d="M2 1 L6 4 L2 7" fill="none" stroke="#fff" stroke-width="1.6"/></svg></span>Sports &amp; Fitness</li>
      <li><span class="bullet"><svg width="8" height="8" viewBox="0 0 8 8"><path d="M2 1 L6 4 L2 7" fill="none" stroke="#fff" stroke-width="1.6"/></svg></span>Crafts &amp; Party Supplies</li>
      <li><span class="bullet"><svg width="8" height="8" viewBox="0 0 8 8"><path d="M2 1 L6 4 L2 7" fill="none" stroke="#fff" stroke-width="1.6"/></svg></span>Pharmacy, Health &amp; Beauty</li>
    </ul>
  </section>

  <section class="side-box news-box">
    <div class="side-title">Newsletter Signup</div>
    <div class="news-row"><div class="field">Your Email Address</div><span class="go-btn">&gt;&gt;</span></div>
  </section>

  <section class="side-box bookmark-box">
    <div class="bookmark-title">
      <svg width="22" height="22" viewBox="0 0 22 22"><rect x="2" y="8" width="16" height="6" rx="2" transform="rotate(-45 11 11)" fill="#e03b3b"/></svg>
      Bookmark Us
    </div>
    <div class="social-row">
      <span style="background:#3b5c9e"></span><span style="background:#3fb3e6"></span><span style="background:#444"></span><span style="background:#2f6fbf"></span><span style="background:#f27a1c"></span><span style="background:#ccc"></span>
    </div>
  </section>

  <div class="pay-row">
    <span class="pay-chip">Solvia</span><span class="pay-chip">Orbcard</span><span class="pay-chip">Distra</span><span class="pay-chip">Crestline</span><span class="pay-chip">Coinvaro</span>
  </div>
</aside>

<main>
  <section class="summer-banner">
    <div class="summer-title">Best <em>Summer</em> Collection</div>
    <div class="summer-strip">Buy Bicycles | Latest Accessories | Latest Collection</div>
    <div class="summer-art" role="img" aria-label="Summer t-shirts, beach bag and sunglasses"></div>
  </section>

  <h2 class="section-head featured">
    <svg width="30" height="30" viewBox="0 0 30 30"><path d="M4 26 Q6 10 18 10 V4 L28 13 L18 22 V16 Q10 16 4 26Z" fill="var(--orange)"/></svg>
    Featured Products
  </h2>
  <section class="product-panel grey">
    <div class="product-card"><div class="product-img" role="img" aria-label="Checked summer shorts" style="background:linear-gradient(#d9c9c4,#9a8a86)"></div><div class="product-name">Summer<br>Shorts</div><div class="price">Price: $9.78</div><div class="buy-btn">🛒 Buy Now</div></div>
    <div class="product-card"><div class="product-img" role="img" aria-label="Beach bag with sunglasses and lotion" style="background:linear-gradient(#f08a6a,#58b36a)"></div><div class="product-name">Beach Bag<br>Essentials</div><div class="price">Price: $9.78</div><div class="buy-btn">🛒 Buy Now</div></div>
    <div class="product-card"><div class="product-img" role="img" aria-label="Green and striped summer shirts" style="background:linear-gradient(#4da65c,#d8dde2)"></div><div class="product-name">Summer Shirts</div><div class="price">Price: $9.78</div><div class="buy-btn">🛒 Buy Now</div></div>
    <div class="product-card"><div class="product-img" role="img" aria-label="Dark grey graphic summer shirt" style="background:linear-gradient(#6a6d72,#45484d)"></div><div class="product-name">Summer<br>Shorts</div><div class="price">Price: $9.78</div><div class="buy-btn">🛒 Buy Now</div></div>
    <div class="product-card"><div class="product-img" role="img" aria-label="Black baby stroller" style="background:linear-gradient(#bdbdbd,#3a3a3a)"></div><div class="product-name">Premium<br>Stroller</div><div class="price">Price: $9.78</div><div class="buy-btn">🛒 Buy Now</div></div>
  </section>

  <h2 class="section-head latest">
    <svg width="30" height="30" viewBox="0 0 30 30"><path d="M4 26 Q6 10 18 10 V4 L28 13 L18 22 V16 Q10 16 4 26Z" fill="#666"/></svg>
    Latest Items
  </h2>
  <section class="product-panel blue">
    <div class="product-card"><div class="product-img" role="img" aria-label="Checked summer shorts" style="background:linear-gradient(#d9c9c4,#9a8a86)"></div><div class="product-name">Summer<br>Shorts</div><div class="price">Price: $9.78</div><div class="buy-btn">🛒 Buy Now</div></div>
    <div class="product-card"><div class="product-img" role="img" aria-label="Beach bag with sunglasses and lotion" style="background:linear-gradient(#f08a6a,#58b36a)"></div><div class="product-name">Beach Bag<br>Essentials</div><div class="price">Price: $9.78</div><div class="buy-btn">🛒 Buy Now</div></div>
    <div class="product-card"><div class="product-img" role="img" aria-label="Green and striped summer shirts" style="background:linear-gradient(#4da65c,#d8dde2)"></div><div class="product-name">Summer Shirts</div><div class="price">Price: $9.78</div><div class="buy-btn">🛒 Buy Now</div></div>
    <div class="product-card"><div class="product-img" role="img" aria-label="Dark grey graphic summer shirt" style="background:linear-gradient(#6a6d72,#45484d)"></div><div class="product-name">Summer<br>Shorts</div><div class="price">Price: $9.78</div><div class="buy-btn">🛒 Buy Now</div></div>
    <div class="product-card"><div class="product-img" role="img" aria-label="Black baby stroller" style="background:linear-gradient(#bdbdbd,#3a3a3a)"></div><div class="product-name">Premium<br>Stroller</div><div class="price">Price: $9.78</div><div class="buy-btn">🛒 Buy Now</div></div>
  </section>
</main>

<aside>
  <section class="promo promo-offer offer-10">
    <div class="promo-img" role="img" aria-label="Green and striped t-shirts" style="background:linear-gradient(135deg,#4da65c,#dfe3e8)"></div>
    <div class="offer-text">
      <div class="offer-big">10% Off</div>
      <div class="offer-sub">For Limited Period</div>
      <div class="offer-note">catch the offer<br>to quench the thirst<br>of entertainment</div>
    </div>
  </section>
  <section class="promo promo-offer offer-25">
    <div class="promo-img" role="img" aria-label="White sports water bottles" style="background:linear-gradient(135deg,#f2f2f2,#9a9a9a)"></div>
    <div class="offer-text">
      <div class="offer-big">25% Off</div>
      <div class="offer-sub">on Latest Movies</div>
      <div class="offer-note">We bet, it's an<br>amazing offer on<br>the whole Web</div>
    </div>
  </section>
  <section class="promo support">
    <div class="support-title"><span class="hours">24/7</span><br>Support<br>Center</div>
    <svg class="headset-icon" width="74" height="92" viewBox="0 0 80 100"><path d="M12 50 V40 A28 28 0 0 1 68 40 V50" fill="none" stroke="#333" stroke-width="6"/><rect x="4" y="44" width="18" height="30" rx="7" fill="#222"/><rect x="58" y="44" width="18" height="30" rx="7" fill="#222"/><path d="M14 74 Q16 92 40 92" fill="none" stroke="#222" stroke-width="3"/></svg>
    <div class="support-note">Registered members get<br>additional benefits over a guest</div>
  </section>
  <section class="promo mega">
    <div class="mega-text">Click here<br>for amazing<strong>mega deals</strong></div>
    <svg class="mega-arrow" width="56" height="40" viewBox="0 0 70 50"><path d="M62 4 Q60 34 24 34 V46 L4 28 L24 10 V22 Q50 22 62 4Z" fill="#fff"/></svg>
  </section>
</aside>

<footer class="site-footer">
  <div class="footer-col" style="left:220px"><h3>Company Info</h3><ul><li>- About Our Company</li><li>- Investor Relations</li><li>- Careers</li><li>- Become an Affiliate</li></ul></div>
  <div class="footer-col" style="left:426px"><h3>Help Center</h3><ul><li>- Returns Policy</li><li>- Privacy Policy</li><li>- Help Topics</li><li>- FAQs</li></ul></div>
  <div class="footer-col" style="left:629px"><h3>Account Info</h3><ul><li>- My Account</li><li>- Order History</li><li>- Shopping Cart</li><li>- Return an Item</li></ul></div>
  <div class="footer-col" style="left:847px"><h3>Shopping</h3><ul><li>- Rewards Solvia</li><li>- Best Price Guarantee</li><li>- Site Map</li><li>- Buying Guides</li></ul></div>
</footer>

</div>
</body>
</html>
```